WP website design (Whitlock)

We need a wordpress design for an established auction and real estate company based in Daswon Creek, Canada. The winning design will incorporate a professional color scheme with company logo in a clean layout with specified widgets. The design needs to consider that this will be developed on a responsive theme. Colors will complement logo - red, black and gray.

Industry/Entity Type

Real Estate

Font styles to use
Sans Serif

Requirements
Must have
• Must Have:
the main logo is provided and the 'horse' logo shouldbe incorporated into the hearder or sidebar (either left or right)as well. Contact info should be placed in the header, and footer too: (250) 555-0143
(250) 555-0178
(250) 555-0192
rvm@zorquil.bc.ca

- Navigation:
1) Home 2) Auctions 3) Online Auctions 4) About Us 5) Contact Us

Home Page will have following:
"Family owned and operated with a family guarantee.
Located in Marrowfield, Canada

Competitive Rates Bonded & Licensed Livestock Dealers & Auctioneers
All Types of Auction Sales in B.C. & Alberta

Farm, Machinery
Equipment Sales
Household & Estate Sales
Livestock Marketing Consultants
Field Cattle Sales
Livestock Pedigree Sales
Horse Sales Appraisals"

Homepage will have auctions - as at http://brindlevexsales.com/upcoming-auctions/.

Footer will have smaller company logo, credit card logo, and attached association logos and this contact info:
.(620) 555-0117: OFFICE
(620) 555-0164: FAX
hgrup@vxq.com: email
Address: 718 N. Birch Ave., Orlin, OK
Mailing Address: PO Box 839, Orlin, OK

Widgets:
1) email sign up 2) News blog widget 3) testimonial blog widget 4) featured auctions widget 5) the 'Gold Peg' logo which is included
Nice to have
• Nice to Have:
- demonstrate the drop-down menu styling, e.g. under Auctions
- Upcoming Auctions
- Past Auctions

```html
<!DOCTYPE html>
<html lang="en">
<head>
<meta charset="utf-8">
<title>Whitlock's Auction Mart Ltd.</title>
<link rel="stylesheet" href="https://fonts.googleapis.com/css2?family=Open+Sans:ital,wght@0,400;0,600;0,700;1,400&display=swap">
<style>
:root{
  --red:#d7141b;
  --dark:#2b2b2b;
  --ink:#333;
  --gray:#888;
  --light:#f6f6f6;
  --line:#e2e2e2;
  --bar:#3c3c3c;
}
*{box-sizing:border-box;margin:0;padding:0}
html,body{width:1200px;height:2575px;overflow:hidden}
body{font-family:"Open Sans",Arial,sans-serif;color:var(--ink);background:#fff;position:relative;border-top:4px solid var(--red)}
.abs{position:absolute}
/* header */
.header{position:absolute;left:0;top:4px;width:1200px;height:147px;background:#fff}
.brand{left:112px;top:26px;width:210px;text-align:center;font-weight:700;font-size:17px;line-height:22px;color:var(--dark);white-space:nowrap}
.brand .mark{display:block;width:30px;height:30px;border-radius:50%;background:var(--dark);margin:10px auto 0}
.contact-top{left:416px;top:24px;font-size:13px;color:#555;display:flex;align-items:center;gap:10px;white-space:nowrap}
.contact-top .lbl{color:#999}
.mail{left:852px;top:24px;font-size:13px;color:var(--red);display:flex;align-items:center;gap:10px;white-space:nowrap}
.nav{left:471px;top:88px;display:flex;font-size:12px;text-transform:uppercase;color:#333;white-space:nowrap}
.nav a{color:inherit;text-decoration:none;padding:7px 16px;border-radius:16px}
.nav a.active{background:#3a3a3a;color:#fff;padding:7px 20px}
.horse{left:1016px;top:18px;width:56px;height:122px;background:#1a1a1a;border-radius:6px}
/* hero */
.hero{left:0;top:151px;width:1200px;height:541px;background:linear-gradient(180deg,#8fb0d6 0%,#b9c9d8 35%,#a89478 60%,#6e7a4a 100%)}
.cap-red{left:135px;top:195px;padding:14px 18px;background:var(--red);color:#fff;font-size:19px;width:515px;white-space:nowrap}
.cap-dark{left:135px;top:270px;padding:12px 16px;background:rgba(40,40,40,.72);color:#fff;font-size:26px;width:515px;white-space:nowrap}
.arrow{width:38px;height:38px;border-radius:50%;background:rgba(255,255,255,.75);top:252px}
.arrow svg{display:block;margin:11px auto}
/* intro */
.tagline{left:0;top:716px;width:1200px;text-align:center;font-style:italic;font-size:27px;color:#444}
.tagline-sub{left:0;top:768px;width:1200px;text-align:center;font-style:italic;font-size:22px;color:var(--red)}
.rule{left:0;top:822px;width:1200px;height:1px;background:var(--line);box-shadow:0 4px 0 #f3f3f3}
/* featured */
.feat-head{left:0;top:858px;width:1200px;display:flex;justify-content:center;align-items:center;gap:16px;font-size:24px;font-weight:600;color:#222}
.dot{width:22px;height:22px;border-radius:50%;display:flex;align-items:center;justify-content:center}
.dot.off{background:#ccc}.dot.on{background:var(--red)}
.card{width:215px;height:290px;background:linear-gradient(#fff,#ececec);border:1px solid #ddd}
.card .pic{height:145px}
.card h3{font-size:13px;font-weight:600;color:var(--red);text-align:center;margin-top:17px}
.card p{font-size:11.5px;color:#aaa;text-align:center;line-height:18px;margin:8px 14px 0}
.card .meta{position:absolute;left:18px;bottom:18px;display:flex;gap:7px}
.card .meta i{display:block;width:12px;height:11px;background:#bbb;border-radius:2px}
.card .bid{position:absolute;left:104px;bottom:12px;width:88px;height:26px;border-radius:13px;background:#2f2f2f;color:#fff;font-size:11px;font-weight:600;text-align:center;line-height:26px}
/* newsletter */
.news-band{left:0;top:1571px;width:1200px;height:315px;background:linear-gradient(180deg,#6b5e5e 0%,#c87a3a 40%,#e59a45 55%,#5a4a40 80%,#3d3a3c 100%)}
.env{left:565px;top:1605px;width:70px;height:70px;border:2px solid #fff;border-radius:50%}
.env span{position:absolute;inset:6px;border-radius:50%;background:#fff;display:flex;align-items:center;justify-content:center}
.nl-title{left:0;top:1688px;width:1200px;text-align:center;color:#fff;font-size:22px;font-weight:600}
.nl-text{left:320px;top:1733px;width:560px;text-align:center;color:#fff;font-size:12px;line-height:21px}
.nl-input{left:343px;top:1801px;width:388px;height:46px;border:2px solid #fff;color:#fff;font-size:12px;padding:13px 14px}
.nl-btn{left:752px;top:1801px;width:138px;height:46px;border-radius:8px;background:#fff;color:#222;font-size:16px;font-weight:600;text-align:center;line-height:46px}
/* news + testimonial */
.lower{left:0;top:1886px;width:1200px;height:376px;background:#f8f8f8}
.sec-title{font-size:24px;font-weight:600;color:#222;display:flex;align-items:center;gap:18px}
.sec-title::after{content:"";height:1px;background:#ddd;flex:1}
.post{width:570px;display:flex;gap:30px}
.post .date{width:50px;text-align:center;color:var(--red);font-size:36px;line-height:36px}
.post .date small{display:block;font-size:19px;color:#333;line-height:24px}
.post h4{font-size:21px;font-weight:400;color:#222;margin-bottom:10px}
.post p{font-size:13px;line-height:22px;color:#777}
.post p b{color:var(--red);font-weight:400}
.quote{left:768px;top:1988px;width:300px;height:210px;background:#eaeaea}
.quote p{font-size:13px;line-height:23px;color:#666;text-align:center;text-transform:uppercase;margin:18px 30px 0}
.quote .q{position:absolute;font-size:34px;color:#aaa;font-family:Georgia,serif}
.quote .who{position:absolute;left:26px;top:140px;display:flex;align-items:center;gap:26px;color:var(--red);font-size:13px}
.avatar{width:56px;height:56px;border-radius:50%;background:linear-gradient(#cfcfcf,#8a8a8a)}
/* contact strip */
.strip{left:0;top:2262px;width:1200px;height:115px;background:#ededed;border-top:1px solid #ddd;border-bottom:1px solid #ddd}
.cell{position:absolute;top:0;height:113px;border-left:1px solid #d8d8d8;text-align:center;font-size:12px;color:#444;white-space:nowrap}
.cell .ic{width:38px;height:38px;border-radius:50%;border:2px solid #999;margin:20px auto 14px;display:flex;align-items:center;justify-content:center}
.cell b{color:var(--red);font-weight:400}
/* footer */
.foot-brand{left:122px;top:2418px;width:112px;text-align:center;font-size:10px;font-weight:700;line-height:13px;color:var(--dark)}
.foot-brand .mark{display:block;width:16px;height:16px;border-radius:50%;background:var(--dark);margin:5px auto 0}
.vsep{width:1px;height:50px;background:#ccc;top:2420px}
.peg{left:260px;top:2418px;width:102px;height:52px;border:2px solid #333;display:flex;align-items:center;justify-content:center;font-size:14px;font-weight:700;color:var(--red)}
.pay-lbl{left:417px;top:2436px;font-size:14px;color:#444}
.card-name{top:2425px;height:44px;border:1px solid #ccc;background:#fff;font-size:15px;font-weight:700;color:#333;display:flex;align-items:center;justify-content:center}
.follow{left:793px;top:2436px;font-size:14px;color:#444}
.soc{top:2428px;width:36px;height:36px;border-radius:50%;border:2px solid #3a78c9;font-size:10px;font-weight:600;color:#3a78c9;display:flex;align-items:center;justify-content:center}
.bottom{left:0;top:2505px;width:1200px;height:70px;background:var(--bar);border-bottom:4px solid var(--red);color:#ccc;font-size:12px;text-align:center;line-height:66px}
.bottom b{color:#fff;font-weight:400}
</style>
</head>
<body>

<header class="header">
  <div class="abs brand">WHITLOCK'S AUCTION<br>MART LTD.<span class="mark"></span></div>
  <div class="abs contact-top">
    <svg width="18" height="18" viewBox="0 0 24 24"><path fill="#333" d="M6.6 10.8a15 15 0 0 0 6.6 6.6l2.2-2.2c.3-.3.7-.4 1-.2 1.1.4 2.3.6 3.6.6.6 0 1 .4 1 1V20c0 .6-.4 1-1 1A17 17 0 0 1 3 4c0-.6.4-1 1-1h3.5c.6 0 1 .4 1 1 0 1.3.2 2.5.6 3.6.1.3 0 .7-.2 1z"/></svg>
    <span><span class="lbl">CALL US:</span> (250) 555-0143,</span>
    <span>(250) 555-0178,</span>
    <span>(250) 555-0192</span>
  </div>
  <div class="abs mail"><svg width="20" height="14" viewBox="0 0 20 14"><rect width="20" height="14" fill="#333"/><path d="M0 0l10 8 10-8" fill="none" stroke="#fff" stroke-width="1.5"/></svg>rvm@zorquil.bc.ca</div>
  <nav class="abs nav">
    <a class="active" href="#">Home</a><a href="#">Auctions</a><a href="#">Online Auctions</a><a href="#">About Us</a><a href="#">Contact Us</a>
  </nav>
  <div class="abs horse" role="img" aria-label="Black horse head emblem"></div>
</header>

<section class="abs hero" role="img" aria-label="Large stone family home with arched windows under a blue sky">
  <div class="abs cap-red">Family owned and operated with a family guarantee</div>
  <div class="abs cap-dark">Located in Marrowfield, Canada</div>
  <div class="abs arrow" style="left:8px"><svg width="14" height="16" viewBox="0 0 14 16"><path d="M10 2L4 8l6 6" fill="none" stroke="#777" stroke-width="2.5"/></svg></div>
  <div class="abs arrow" style="left:1144px"><svg width="14" height="16" viewBox="0 0 14 16"><path d="M4 2l6 6-6 6" fill="none" stroke="#777" stroke-width="2.5"/></svg></div>
</section>

<p class="abs tagline">Competitive Rates Bonded &amp; Licensed Livestock Dealers &amp; Auctioneers</p>
<p class="abs tagline-sub">All Types of Auction Sales in B.C. &amp; Alberta</p>
<div class="abs rule"></div>

<h2 class="abs feat-head">
  <span class="dot off"><svg width="8" height="10" viewBox="0 0 8 10"><path d="M6 1L2 5l4 4" fill="none" stroke="#fff" stroke-width="2"/></svg></span>
  Featured Auctions
  <span class="dot on"><svg width="8" height="10" viewBox="0 0 8 10"><path d="M2 1l4 4-4 4" fill="none" stroke="#fff" stroke-width="2"/></svg></span>
</h2>

<div class="abs card" style="left:130px;top:918px"><div class="pic" role="img" aria-label="Two-storey stone house" style="background:linear-gradient(#a9c4e0,#8b7a62 60%,#5d7a3a)"></div><h3>NEQUE PORRO QUISQ</h3><p>Lorem ipsum dolor sit amet, cons etur adipisicing elit, sed do.</p><div class="meta"><i></i><i></i><i></i></div><div class="bid">BID NOW</div></div>
<div class="abs card" style="left:373px;top:918px"><div class="pic" role="img" aria-label="Brick family home with lawn" style="background:linear-gradient(#8fb8e6,#a0644a 55%,#5f8d3a)"></div><h3>NEQUE PORRO QUISQ</h3><p>Lorem ipsum dolor sit amet, cons etur adipisicing elit, sed do.</p><div class="meta"><i></i><i></i><i></i></div><div class="bid">BID NOW</div></div>
<div class="abs card" style="left:613px;top:918px"><div class="pic" role="img" aria-label="Wooden farmhouse beside a pond" style="background:linear-gradient(#3f8fe0,#7a6a55 50%,#3b7fb0)"></div><h3>NEQUE PORRO QUISQ</h3><p>Lorem ipsum dolor sit amet, cons etur adipisicing elit, sed do.</p><div class="meta"><i></i><i></i><i></i></div><div class="bid">BID NOW</div></div>
<div class="abs card" style="left:853px;top:918px"><div class="pic" role="img" aria-label="Large house with triple garage" style="background:linear-gradient(#b7cde0,#b09a85 55%,#9a9a9a)"></div><h3>NEQUE PORRO QUISQ</h3><p>Lorem ipsum dolor sit amet, cons etur adipisicing elit, sed do.</p><div class="meta"><i></i><i></i><i></i></div><div class="bid">BID NOW</div></div>

<div class="abs card" style="left:130px;top:1240px"><div class="pic" role="img" aria-label="Yellow villa with garden" style="background:linear-gradient(#4f90e0,#d6b06a 55%,#4f8a30)"></div><h3>NEQUE PORRO QUISQ</h3><p>Lorem ipsum dolor sit amet, cons etur adipisicing elit, sed do.</p><div class="meta"><i></i><i></i><i></i></div><div class="bid">BID NOW</div></div>
<div class="abs card" style="left:373px;top:1240px"><div class="pic" role="img" aria-label="Lakeside cottage among trees" style="background:linear-gradient(#c9dde8,#3c5a38 45%,#3e6e8c)"></div><h3>NEQUE PORRO QUISQ</h3><p>Lorem ipsum dolor sit amet, cons etur adipisicing elit, sed do.</p><div class="meta"><i></i><i></i><i></i></div><div class="bid">BID NOW</div></div>
<div class="abs card" style="left:613px;top:1240px"><div class="pic" role="img" aria-label="Family in front of a suburban house" style="background:linear-gradient(#a8c6e8,#9a9a8a 50%,#5a8c3a)"></div><h3>NEQUE PORRO QUISQ</h3><p>Lorem ipsum dolor sit amet, cons etur adipisicing elit, sed do.</p><div class="meta"><i></i><i></i><i></i></div><div class="bid">BID NOW</div></div>
<div class="abs card" style="left:853px;top:1240px"><div class="pic" role="img" aria-label="Mediterranean style home" style="background:linear-gradient(#3d86d8,#d4b27a 55%,#6f8a3a)"></div><h3>NEQUE PORRO QUISQ</h3><p>Lorem ipsum dolor sit amet, cons etur adipisicing elit, sed do.</p><div class="meta"><i></i><i></i><i></i></div><div class="bid">BID NOW</div></div>

<section class="abs news-band" role="img" aria-label="City skyline at sunset"></section>
<div class="abs env"><span><svg width="26" height="18" viewBox="0 0 26 18"><rect width="26" height="18" rx="2" fill="#999"/><path d="M1 1l12 9 12-9" fill="none" stroke="#fff" stroke-width="2"/></svg></span></div>
<h2 class="abs nl-title">eMail Sign up Newsletter</h2>
<p class="abs nl-text">At vero eos et accusamus et iusto odio dignissimos ducimus qui blanditiis praesentium voluptas dolores et quas molestias excepturi sint occaecati cupiditate non provident,</p>
<div class="abs nl-input">Enter email Address:</div>
<div class="abs nl-btn">SUBSCRIBE</div>

<section class="abs lower">
  <h2 class="abs sec-title" style="left:130px;top:40px;width:575px">Latest News</h2>
  <article class="abs post" style="left:130px;top:98px">
    <div class="date">28<small>Apr</small></div>
    <div><h4>Neque porro quisquam</h4><p>Sed ut perspiciatis unde omnis iste natus error sit voluptatem accusantium dol totam rem aperiam, eaque ipsa quae ab illo inventore veritatis et lorem ipsum sunt explicabo. Nemo enim ipsam voluptatem. <b>Read More</b></p></div>
  </article>
  <article class="abs post" style="left:130px;top:232px">
    <div class="date">28<small>Apr</small></div>
    <div><h4>Neque porro quisquam</h4><p>Sed ut perspiciatis unde omnis iste natus error sit voluptatem accusantium dol totam rem aperiam, eaque ipsa quae ab illo inventore veritatis et lorem ipsum sunt explicabo. Nemo enim ipsam voluptatem. <b>Read More</b></p></div>
  </article>
  <h2 class="abs sec-title" style="left:768px;top:40px;width:300px">Testimonial</h2>
</section>
<div class="abs quote">
  <span class="q" style="left:10px;top:2px">&ldquo;</span>
  <p>Sed ut perspiciatis unde omnis totam rem aperiam, eaque ipsa qua sunt explicabo. Nemo eni.</p>
  <span class="q" style="right:26px;top:70px">&rdquo;</span>
  <div class="who"><div class="avatar" role="img" aria-label="Portrait of the client"></div>Tarek Olwen, city name</div>
</div>

<section class="abs strip">
  <div class="cell" style="left:115px;width:167px"><div class="ic"><svg width="14" height="14" viewBox="0 0 14 14"><rect x="2" y="1" width="10" height="12" fill="#999"/></svg></div>(620) 555-0117: <b>OFFICE,</b></div>
  <div class="cell" style="left:282px;width:140px"><div class="ic"><svg width="16" height="14" viewBox="0 0 16 14"><rect x="1" y="4" width="14" height="9" fill="#999"/><rect x="4" y="1" width="8" height="4" fill="#999"/></svg></div>(620) 555-0164: <b>FAX,</b></div>
  <div class="cell" style="left:422px;width:162px"><div class="ic"><svg width="16" height="12" viewBox="0 0 16 12"><rect width="16" height="12" fill="#999"/><path d="M0 0l8 6 8-6" fill="none" stroke="#fff"/></svg></div>hgrup@vxq.com: <b>email,</b></div>
  <div class="cell" style="left:584px;width:234px"><div class="ic"><svg width="12" height="16" viewBox="0 0 12 16"><path d="M6 0a6 6 0 0 1 6 6c0 4-6 10-6 10S0 10 0 6a6 6 0 0 1 6-6z" fill="#999"/><circle cx="6" cy="6" r="2" fill="#fff"/></svg></div><b>Address:</b> 718 N. Birch Ave., Orlin, OK,</div>
  <div class="cell" style="left:818px;width:265px;border-right:1px solid #d8d8d8"><div class="ic"><svg width="16" height="14" viewBox="0 0 16 14"><rect x="1" y="3" width="14" height="10" rx="2" fill="#999"/><circle cx="8" cy="8" r="3" fill="#fff"/></svg></div><b>Mailing Address:</b> PO Box 839, Orlin, OK</div>
</section>

<footer>
  <div class="abs foot-brand">WHITLOCK'S AUCTION<br>MART LTD.<span class="mark"></span></div>
  <div class="abs vsep" style="left:240px"></div>
  <div class="abs peg">Gold Peg</div>
  <div class="abs vsep" style="left:393px"></div>
  <div class="abs pay-lbl">PAYMENT</div>
  <div class="abs card-name" style="left:506px;width:74px">Varda</div>
  <div class="abs card-name" style="left:586px;width:78px">Merix</div>
  <div class="abs card-name" style="left:670px;width:74px">Dovel</div>
  <div class="abs vsep" style="left:768px"></div>
  <div class="abs follow">FOLLOW US</div>
  <div class="abs soc" style="left:891px">Ovo</div>
  <div class="abs soc" style="left:935px">Kel</div>
  <div class="abs soc" style="left:979px">Zim</div>
  <div class="abs soc" style="left:1023px">Rue</div>
  <div class="abs bottom">Copyright © 2014 all rights are reserved <b>Whitlocks privacy &amp; Policy</b></div>
</footer>

</body>
</html>
```